Business card for consulting firm

We need a double-sided business card for consulting firm, VantoriX. The card should be professional but also creative and visually interesting.

Target Market(s)

Engineering and technology; transport industries; safety critical / heavy industry.

Contact Information for Business Card

See attached file with details.

Font styles to use
Sans Serif

```html
<!DOCTYPE html>
<html lang="en">
<head>
<meta charset="utf-8">
<title>VantoriX Business Card</title>
<link href="https://fonts.googleapis.com/css2?family=Lato:wght@400;700;900&display=swap" rel="stylesheet">
<style>
  :root {
    --stage: #2b2b30;
    --sky: #1fb8e6;
    --sky-light: #5ccbee;
    --paper: #ffffff;
    --navy: #2b1f5e;
    --plum: #932f9f;
    --ink: #3a3550;
  }
  * { margin: 0; padding: 0; box-sizing: border-box; }
  html, body { width: 1200px; height: 801px; overflow: hidden; }
  body {
    background: var(--stage);
    font-family: "Lato", sans-serif;
    position: relative;
  }
  .card {
    position: absolute;
    top: 246px;
    width: 540px;
    height: 309px;
    border-radius: 22px;
    overflow: hidden;
  }
  .card--front { left: 40px; background: var(--sky); }
  .card--back { left: 620px; background: var(--paper); }

  .front-pattern {
    position: absolute;
    left: 0; top: 0; right: 0;
    height: 170px;
    background: linear-gradient(180deg, var(--sky-light) 0%, var(--sky) 100%);
  }
  .front-brand {
    position: absolute;
    left: 0; right: 0; top: 118px;
    text-align: center;
    color: var(--paper);
  }
  .brand-name {
    font-weight: 900;
    font-size: 54px;
    letter-spacing: 1px;
    line-height: 1;
  }
  .brand-tagline {
    font-weight: 400;
    font-size: 17px;
    letter-spacing: 0.5px;
    margin-top: 6px;
  }

  .back-brand {
    position: absolute;
    left: 34px; top: 60px;
    color: var(--navy);
  }
  .back-brand .brand-name { font-size: 46px; }
  .back-brand .brand-tagline { font-size: 15px; color: var(--ink); }

  .person {
    position: absolute;
    left: 34px; bottom: 40px;
  }
  .person-name {
    font-weight: 900;
    font-size: 22px;
    color: var(--navy);
  }
  .person-credentials {
    font-size: 13px;
    color: var(--plum);
    margin-top: 4px;
  }
  .person-role {
    font-weight: 700;
    font-size: 13px;
    color: var(--plum);
    margin-top: 2px;
  }

  .contact {
    position: absolute;
    right: 28px; top: 70px;
    list-style: none;
    font-size: 12.5px;
    color: var(--ink);
  }
  .contact li {
    display: flex;
    align-items: center;
    gap: 8px;
    margin-bottom: 9px;
  }
  .contact svg { width: 13px; height: 13px; flex: none; }
</style>
</head>
<body>
  <section class="card card--front">
    <div class="front-pattern" role="img" aria-label="Soft pattern of light blue rounded blobs"></div>
    <div class="front-brand">
      <div class="brand-name">VantoriX</div>
      <div class="brand-tagline">Safety &amp; Human Factors</div>
    </div>
  </section>

  <section class="card card--back">
    <div class="back-brand">
      <div class="brand-name">VantoriX</div>
      <div class="brand-tagline">Safety &amp; Human Factors</div>
    </div>

    <ul class="contact">
      <li>
        <svg viewBox="0 0 16 16"><path fill="#932f9f" d="M3.5 1.5l2.5 0 1 3.5-1.8 1.2a9 9 0 0 0 4.6 4.6L11 9l3.5 1v2.5c0 1-1 2-2 2A11 11 0 0 1 1.5 3.5c0-1 1-2 2-2z"/></svg>
        +61 (0)400 555 018
      </li>
      <li>
        <svg viewBox="0 0 16 16"><rect x="1" y="3" width="14" height="10" rx="1" fill="#932f9f"/><path d="M1.5 4l6.5 5 6.5-5" stroke="#fff" stroke-width="1.3" fill="none"/></svg>
        hcarstairs@vantorix.com.au
      </li>
      <li>
        <svg viewBox="0 0 16 16"><circle cx="8" cy="8" r="7" fill="#932f9f"/><path d="M1 8h14M8 1c-3 3-3 11 0 14M8 1c3 3 3 11 0 14" stroke="#fff" stroke-width="1" fill="none"/></svg>
        www.vantorix.global
      </li>
      <li>
        <svg viewBox="0 0 16 16"><circle cx="8" cy="8" r="7" fill="#932f9f"/><path d="M1 8h14M8 1c-3 3-3 11 0 14M8 1c3 3 3 11 0 14" stroke="#fff" stroke-width="1" fill="none"/></svg>
        www.vantorix.com.au
      </li>
    </ul>

    <div class="person">
      <div class="person-name">Helena Carstairs</div>
      <div class="person-credentials">BA (Hons), M Psych Org, M Tech Mgt (HF)</div>
      <div class="person-role">Managing Director</div>
    </div>
  </section>
</body>
</html>
```